Talbek vodka

With the logo attached in the subsequent file, a business card that reflects a premium and organic vodka. On the first side, the company logo in large. The names must be included on the back of the card (Mateo Ignacio Dalmau Ferrerons with the number +34 655 219 870 and Oriol Batlle Quintana and +34 677 341 592). The slogan "What binds us" and "Organic and permium vodka" in bold E-mail (talbekvodka@mailora.net); Website www.talbekvodkaorg.net

```html
<!DOCTYPE html>
<html lang="en">
<head>
<meta charset="utf-8">
<title>Talbek Vodka – Business Card</title>
<link href="https://fonts.googleapis.com/css2?family=Lato:wght@400;700;900&display=swap" rel="stylesheet">
<style>
  :root {
    --backdrop: #5c5c5c;
    --card: #0a0a0a;
    --ink: #ffffff;
    --muted: #8c8c8c;
    --soft: #a9a9a9;
    --rule: #e6e6e6;
  }
  * { margin: 0; padding: 0; box-sizing: border-box; }
  html, body {
    width: 1200px; height: 960px; overflow: hidden;
    background: var(--backdrop);
    font-family: "Lato", sans-serif;
  }
  .card {
    position: absolute;
    top: 177px;
    width: 364px; height: 637px;
    background: var(--card);
    border-radius: 24px;
    box-shadow: 0 6px 14px rgba(0,0,0,0.35);
  }
  .card--back { left: 168px; }
  .card--front { left: 662px; }

  .line {
    position: absolute; left: 0; width: 100%;
    text-align: center; white-space: nowrap;
  }
  .slogan-title { top: 145px; font-size: 22px; font-weight: 700; color: var(--ink); }
  .slogan-sub   { top: 175px; font-size: 22px; font-weight: 700; color: var(--muted); }

  .contact-name { color: var(--ink); font-weight: 700; }
  .contact-name--first  { top: 399px; font-size: 20px; }
  .contact-name--second { top: 469px; font-size: 25px; }
  .contact-phone {
    font-size: 14px; color: var(--soft); letter-spacing: 0.2px;
    display: flex; justify-content: center; align-items: center; gap: 8px;
  }
  .contact-phone--first  { top: 429px; }
  .contact-phone--second { top: 505px; }
  .phone-icon { width: 14px; height: 12px; fill: var(--ink); }

  .divider {
    position: absolute; left: 52px; width: 260px; height: 1px;
    background: var(--rule);
  }
  .divider--first  { top: 462px; }
  .divider--second { top: 541px; }

  .web-details { font-size: 17px; color: var(--ink); }
  .web-email { top: 557px; }
  .web-site  { top: 584px; }

  .brand {
    position: absolute; left: 0; top: 300px; width: 100%;
    text-align: center;
    font-size: 42px; font-weight: 400; color: var(--muted);
    letter-spacing: 1px;
  }
</style>
</head>
<body>
  <section class="card card--back">
    <p class="line slogan-title">What binds us</p>
    <p class="line slogan-sub">Organic and permium vodka</p>

    <p class="line contact-name contact-name--first">Mateo Ignacio Dalmau Ferrerons</p>
    <p class="line contact-phone contact-phone--first">
      <svg class="phone-icon" viewBox="0 0 14 12" aria-hidden="true">
        <path d="M1 4 Q1 1 7 1 Q13 1 13 4 L13 5 L10 5 L10 3.6 Q7 3 4 3.6 L4 5 L1 5 Z"/>
        <path d="M3 6 L11 6 L12.5 11 L1.5 11 Z"/>
      </svg>
      +34 655 219 870
    </p>
    <div class="divider divider--first"></div>

    <p class="line contact-name contact-name--second">Oriol Batlle Quintana</p>
    <p class="line contact-phone contact-phone--second">
      <svg class="phone-icon" viewBox="0 0 14 12" aria-hidden="true">
        <path d="M1 4 Q1 1 7 1 Q13 1 13 4 L13 5 L10 5 L10 3.6 Q7 3 4 3.6 L4 5 L1 5 Z"/>
        <path d="M3 6 L11 6 L12.5 11 L1.5 11 Z"/>
      </svg>
      +34 677 341 592
    </p>
    <div class="divider divider--second"></div>

    <p class="line web-details web-email">talbekvodka@mailora.net</p>
    <p class="line web-details web-site">www.talbekvodkaorg.net</p>
  </section>

  <section class="card card--front">
    <p class="brand">Talbek Vodka</p>
  </section>
</body>
</html>
```